Design some Business Cards

I need a business card designed, in English on one side, and in Russian on the other side, which will incorporate my client’s logo (logo in different formats is in zip folder attached). The name, details/info required on the business card are in the document in the zip folder.

Please let me know if you have any questions. I will provide feedback on the entries as quickly as I can.

Regards.

```html
<!DOCTYPE html>
<html lang="en">
<head>
<meta charset="utf-8">
<title>Casamar Estates — Business Cards</title>
<link rel="stylesheet" href="https://fonts.googleapis.com/css2?family=Roboto+Slab:wght@400;700&family=Roboto+Condensed:wght@400&display=swap">
<style>
  :root {
    --bg: #e9e9ec;
    --card: #ffffff;
    --orange: #e98a3a;
    --blue: #2a6db5;
    --rule: #9dbde2;
    --ink: #1d1d1f;
    --faint: #d9e3ef;
  }
  * { box-sizing: border-box; margin: 0; padding: 0; }
  html, body { width: 1200px; height: 900px; overflow: hidden; }
  body { background: var(--bg); position: relative; }
  .card {
    position: absolute;
    left: 250px;
    width: 700px;
    height: 400px;
    background: var(--card);
    border-radius: 24px;
    box-shadow: 0 2px 10px rgba(0,0,0,.12);
    overflow: hidden;
  }
  .card--ru { top: 33px; }
  .card--en { top: 467px; }
  .brand {
    position: absolute;
    right: 40px;
    top: 46px;
    font-family: "Roboto Slab", serif;
    font-weight: 400;
    font-size: 28px;
    letter-spacing: 2px;
    color: var(--blue);
  }
  .brand--faint {
    right: 110px;
    top: 128px;
    color: var(--faint);
  }
  .rule-top {
    position: absolute;
    left: 300px;
    right: 0;
    top: 98px;
    height: 1px;
    background: var(--rule);
  }
  .person { position: absolute; left: 40px; top: 168px; }
  .person__name {
    font-family: "Roboto Slab", serif;
    font-weight: 700;
    font-size: 30px;
    line-height: 1.1;
  }
  .person__first { color: var(--orange); }
  .person__last { color: var(--blue); }
  .person__role {
    font-family: "Roboto Slab", serif;
    font-weight: 700;
    font-size: 15px;
    color: var(--ink);
    margin-top: 4px;
  }
  .rule-name {
    position: absolute;
    left: 40px;
    width: 340px;
    top: 245px;
    height: 1px;
    background: var(--rule);
  }
  .contacts {
    position: absolute;
    left: 40px;
    top: 272px;
    list-style: none;
    font-family: "Roboto Condensed", sans-serif;
    font-size: 16px;
    color: var(--ink);
  }
  .contacts li {
    display: flex;
    align-items: center;
    height: 27px;
  }
  .contacts svg {
    width: 14px;
    height: 14px;
    margin-right: 14px;
    fill: var(--blue);
    flex: none;
  }
</style>
</head>
<body>

<section class="card card--ru" lang="ru">
  <div class="brand">CASAMAR ESTATES</div>
  <div class="rule-top"></div>
  <div class="brand brand--faint" aria-hidden="true">CASAMAR ESTATES</div>
  <div class="person">
    <div class="person__name"><span class="person__first">Марина</span> <span class="person__last">Соколенко</span></div>
    <div class="person__role">Директор</div>
  </div>
  <div class="rule-name"></div>
  <ul class="contacts">
    <li><svg viewBox="0 0 24 24"><path d="M6.6 10.8a15.1 15.1 0 0 0 6.6 6.6l2.2-2.2a1 1 0 0 1 1-.25 11.4 11.4 0 0 0 3.6.57 1 1 0 0 1 1 1V20a1 1 0 0 1-1 1A17 17 0 0 1 3 4a1 1 0 0 1 1-1h3.5a1 1 0 0 1 1 1c0 1.25.2 2.45.57 3.57a1 1 0 0 1-.25 1z"/></svg>+38 044 555 01 20</li>
    <li><svg viewBox="0 0 24 24"><path d="M6.6 10.8a15.1 15.1 0 0 0 6.6 6.6l2.2-2.2a1 1 0 0 1 1-.25 11.4 11.4 0 0 0 3.6.57 1 1 0 0 1 1 1V20a1 1 0 0 1-1 1A17 17 0 0 1 3 4a1 1 0 0 1 1-1h3.5a1 1 0 0 1 1 1c0 1.25.2 2.45.57 3.57a1 1 0 0 1-.25 1z"/></svg>+34 600 555 123</li>
    <li><svg viewBox="0 0 24 24"><path d="M2 11 22 2l-9 20-2.5-8.5z"/></svg>marina@casamarestates.com</li>
    <li><svg viewBox="0 0 24 24"><path d="M12 2a10 10 0 1 0 0 20 10 10 0 0 0 0-20zm6.9 9h-3a15 15 0 0 0-1.3-5.9A8 8 0 0 1 18.9 11zM12 4.1c.9 1.2 1.8 3.6 2 6.9h-4c.2-3.3 1.1-5.7 2-6.9zM9.4 5.1A15 15 0 0 0 8.1 11h-3a8 8 0 0 1 4.3-5.9zM5.1 13h3a15 15 0 0 0 1.3 5.9A8 8 0 0 1 5.1 13zm6.9 6.9c-.9-1.2-1.8-3.6-2-6.9h4c-.2 3.3-1.1 5.7-2 6.9zm2.6-1A15 15 0 0 0 15.9 13h3a8 8 0 0 1-4.3 5.9z"/></svg>www.casamarestates.com</li>
  </ul>
</section>

<section class="card card--en">
  <div class="brand">CASAMAR ESTATES</div>
  <div class="rule-top"></div>
  <div class="person">
    <div class="person__name"><span class="person__first">Marina</span> <span class="person__last">Sokolenko</span></div>
    <div class="person__role">Director</div>
  </div>
  <div class="rule-name"></div>
  <ul class="contacts">
    <li><svg viewBox="0 0 24 24"><path d="M6.6 10.8a15.1 15.1 0 0 0 6.6 6.6l2.2-2.2a1 1 0 0 1 1-.25 11.4 11.4 0 0 0 3.6.57 1 1 0 0 1 1 1V20a1 1 0 0 1-1 1A17 17 0 0 1 3 4a1 1 0 0 1 1-1h3.5a1 1 0 0 1 1 1c0 1.25.2 2.45.57 3.57a1 1 0 0 1-.25 1z"/></svg>+34 600 555 123</li>
    <li><svg viewBox="0 0 24 24"><path d="M2 11 22 2l-9 20-2.5-8.5z"/></svg>marina@casamarestates.com</li>
    <li><svg viewBox="0 0 24 24"><path d="M12 2a10 10 0 1 0 0 20 10 10 0 0 0 0-20zm6.9 9h-3a15 15 0 0 0-1.3-5.9A8 8 0 0 1 18.9 11zM12 4.1c.9 1.2 1.8 3.6 2 6.9h-4c.2-3.3 1.1-5.7 2-6.9zM9.4 5.1A15 15 0 0 0 8.1 11h-3a8 8 0 0 1 4.3-5.9zM5.1 13h3a15 15 0 0 0 1.3 5.9A8 8 0 0 1 5.1 13zm6.9 6.9c-.9-1.2-1.8-3.6-2-6.9h4c-.2 3.3-1.1 5.7-2 6.9zm2.6-1A15 15 0 0 0 15.9 13h3a8 8 0 0 1-4.3 5.9z"/></svg>www.casamarestates.com</li>
  </ul>
</section>

</body>
</html>
```